Back Pain

Need a flyer similar to the attached draft. This is to be handed out to prospective patients. Note that Sketch Hive has already designed the logo. If you need a copy please contact me

```html
<!DOCTYPE html>
<html lang="en">
<head>
<meta charset="utf-8">
<title>Spinewell Clinic – Tech Neck Flyer</title>
<link rel="stylesheet" href="https://fonts.googleapis.com/css2?family=Roboto:wght@300;400;500;700&family=Oswald:wght@500;600&display=swap">
<style>
  :root {
    --green: #8cc63f;
    --green-light: #bfe19b;
    --blue: #1a6db5;
    --blue-dark: #0f5ea6;
    --teal: #2b8f9c;
    --ink: #1d1d1d;
    --page: #e9e6e2;
    --white: #ffffff;
  }
  * { box-sizing: border-box; margin: 0; padding: 0; }
  html, body { width: 1200px; height: 1200px; overflow: hidden; background: var(--page); }
  .flyer {
    position: absolute; left: 187px; top: 20px;
    width: 876px; height: 1229px;
    transform: scale(0.9431); transform-origin: top left;
    background: var(--white); overflow: hidden;
    font-family: "Roboto", Arial, sans-serif; color: var(--ink);
    box-shadow: 0 8px 24px rgba(0,0,0,.18);
  }
  .abs { position: absolute; }
  .hero {
    left: 0; top: 0; width: 876px; height: 500px;
    background: linear-gradient(180deg, #7cc043 0%, #5fae55 22%, #2a9187 48%, #1f7cae 72%, #1a6db5 100%);
  }
  .left-shade {
    left: 0; top: 380px; width: 500px; height: 760px;
    background: linear-gradient(90deg, #ffffff 0%, #ffffff 62%, #ececec 100%);
  }
  .wave { left: 0; top: 320px; width: 876px; height: 200px; }
  .brand { left: 0; top: 127px; width: 876px; text-align: center; color: var(--white); }
  .brand-mark {
    left: 389px; top: 28px; width: 98px; height: 98px;
    border: 5px solid var(--white); border-radius: 50%;
  }
  .brand-name { font-weight: 500; font-size: 21px; letter-spacing: -0.3px; }
  .brand-sub { font-weight: 500; font-size: 10px; letter-spacing: 2.6px; margin-top: 1px; }
  .headline { left: 0; top: 172px; width: 876px; text-align: center; color: var(--white); }
  .headline-top { font-weight: 300; font-size: 74px; line-height: 80px; color: #eef1f0; }
  .headline-main { font-weight: 700; font-size: 82px; line-height: 76px; letter-spacing: -1px; }

  .body-figure {
    left: 43px; top: 498px; width: 162px; height: 403px;
    background: var(--green); border-radius: 60px 60px 10px 10px;
  }
  .callouts { left: 0; top: 480px; width: 500px; height: 420px; }
  .symptom { position: absolute; left: 325px; font-size: 16px; color: var(--ink); }

  .care-title {
    left: 36px; top: 905px; font-family: "Oswald", Arial, sans-serif;
    font-weight: 600; font-size: 46px; color: var(--blue); letter-spacing: -0.5px; transform: scaleX(0.92); transform-origin: left;
  }
  .care-text { left: 36px; top: 958px; width: 460px; font-size: 15.5px; font-weight: 500; line-height: 20.5px; }

  .chart-title {
    left: 540px; top: 486px; font-family: "Oswald", Arial, sans-serif;
    font-weight: 500; font-size: 20px; line-height: 24px; transform: scaleX(0.88); transform-origin: left;
  }
  .g { color: var(--green); } .b { color: var(--blue); }
  .bar { position: absolute; width: 32px; bottom: 406px; display: flex; flex-direction: column; }
  .bar-light { height: 48px; background: repeating-linear-gradient(180deg, var(--green-light) 0 8px, transparent 8px 13px); }
  .bar-dark { flex: 1; background: repeating-linear-gradient(180deg, var(--blue) 0 8px, transparent 8px 13px); }
  .pin {
    position: absolute; width: 28px; height: 28px; border-radius: 50%;
    background: var(--blue); color: var(--white); font-size: 12px; font-weight: 700;
    display: flex; align-items: center; justify-content: center;
  }
  .pin::after {
    content: ""; position: absolute; bottom: -6px; left: 9px;
    border-left: 5px solid transparent; border-right: 5px solid transparent; border-top: 7px solid var(--blue);
  }
  .tick { position: absolute; top: 831px; font-size: 16px; }
  .axis-x { left: 538px; top: 859px; font-size: 16px; }
  .axis-y { left: 822px; top: 823px; font-size: 14px; transform: rotate(-90deg); transform-origin: left top; white-space: nowrap; }

  .donut { left: 529px; top: 897px; width: 108px; height: 108px; }
  .stat {
    left: 646px; top: 904px; font-family: "Oswald", Arial, sans-serif;
    font-weight: 500; font-size: 21px; line-height: 24px; transform: scaleX(0.86); transform-origin: left;
  }

  .footer-band { left: 0; top: 1125px; width: 876px; height: 104px; background: var(--blue); }
  .location-card {
    left: 30px; top: 1033px; width: 545px; height: 135px; background: var(--white);
    border-radius: 6px; box-shadow: 0 3px 8px rgba(0,0,0,.3); text-align: center;
  }
  .doctor { margin-top: 21px; font-size: 24px; font-weight: 500; color: var(--blue); }
  .now-in { font-size: 36px; font-weight: 700; color: var(--green); line-height: 40px; margin-top: 2px; }
  .address { font-size: 24px; color: var(--ink); margin-top: 1px; }
  .offer {
    left: 553px; top: 1033px; width: 293px; height: 135px; background: var(--green);
    border-radius: 0 6px 6px 0; color: var(--white);
    clip-path: polygon(0 0,100% 0,100% 100%,0 100%,4% 92%,0 84%,4% 76%,0 68%,4% 60%,0 52%,4% 44%,0 36%,4% 28%,0 20%,4% 12%,0 6%);
  }
  .offer-pct { position: absolute; left: 46px; top: -4px; font-family: "Oswald", Arial, sans-serif; font-weight: 500; font-size: 96px; line-height: 110px; }
  .offer-off { position: absolute; left: 236px; top: 96px; font-family: "Oswald", Arial, sans-serif; font-weight: 600; font-size: 40px; transform: rotate(-90deg); transform-origin: left top; }
  .offer-note { position: absolute; left: 0; width: 100%; padding-left: 12px; top: 104px; text-align: center; font-size: 18px; }
  .booking { left: 0; top: 1183px; width: 876px; text-align: center; color: var(--white); font-size: 16px; }
</style>
</head>
<body>
<main class="flyer">
  <div class="abs hero"></div>
  <div class="abs left-shade"></div>

  <svg class="abs wave" viewBox="0 0 876 200" role="img" aria-label="Spine vertebrae illustration curving across the header">
    <path d="M0 200 L0 160 C180 120 330 60 500 40 C650 25 760 20 876 45 L876 200 Z" fill="#ffffff"/>
    <path d="M0 160 C180 120 330 60 500 40 C650 25 760 20 876 45 L876 10 C760 -20 640 -25 500 -10 C330 10 180 80 0 125 Z" fill="#e6f0f6" opacity="0.85"/>
  </svg>

  <div class="abs brand-mark"></div>
  <div class="abs brand">
    <div class="brand-name">SPINEWELL CARE CLINIC</div>
    <div class="brand-sub">DR SAM PORTER - CHIROPRACTOR</div>
  </div>
  <div class="abs headline">
    <div class="headline-top">SPINEWELL CLINIC</div>
    <div class="headline-main">TECH NECK</div>
  </div>

  <div class="abs body-figure" role="img" aria-label="Green silhouette of a human upper body"></div>
  <svg class="abs callouts" viewBox="0 0 500 420">
    <g fill="none" stroke="#1a6db5" stroke-width="1.3">
      <polyline points="127,35 180,53 308,53"/>
      <polyline points="127,93 180,77 308,77"/>
      <polyline points="183,118 245,136 308,136"/>
      <polyline points="172,199 245,217 308,217"/>
      <polyline points="200,260 245,276 308,276"/>
      <polyline points="124,268 180,361 245,361 245,379 308,379"/>
    </g>
    <g fill="#1a6db5">
      <circle cx="127" cy="35" r="5"/><circle cx="308" cy="53" r="5"/>
      <circle cx="127" cy="93" r="5"/><circle cx="308" cy="77" r="5"/>
      <circle cx="183" cy="118" r="5"/><circle cx="308" cy="136" r="5"/>
      <circle cx="172" cy="199" r="5"/><circle cx="308" cy="217" r="5"/>
      <circle cx="200" cy="260" r="5"/><circle cx="308" cy="276" r="5"/>
      <circle cx="124" cy="268" r="5"/><circle cx="308" cy="379" r="5"/>
    </g>
  </svg>
  <div class="symptom" style="top:523px">Headaches</div>
  <div class="symptom" style="top:547px">Neck pain</div>
  <div class="symptom" style="top:605px">Shoulder pain</div>
  <div class="symptom" style="top:686px">Back pain</div>
  <div class="symptom" style="top:745px">Arm &amp; Hand pain</div>
  <div class="symptom" style="top:848px">Sciatica</div>

  <div class="abs care-title">CHIROPACTIC CARE</div>
  <div class="abs care-text">CAN HELP CORRECT AND PREVENT THESE PROBLEMS BY RESTORING AND MAINTAINING PROPERALIGNMENT OF THE NECK</div>

  <div class="abs chart-title"><span class="g">AS THE HEAD TILTS FORWARD.</span><br><span class="b">MORE FORCE IS PLACED ON THE SPINE</span></div>

  <div class="bar" style="left:538px;height:72px"><div class="bar-light"></div><div class="bar-dark"></div></div>
  <div class="bar" style="left:598px;height:123px"><div class="bar-light"></div><div class="bar-dark"></div></div>
  <div class="bar" style="left:658px;height:155px"><div class="bar-light" style="height:34px"></div><div class="bar-dark"></div></div>
  <div class="bar" style="left:718px;height:187px"><div class="bar-light" style="height:21px"></div><div class="bar-dark"></div></div>
  <div class="bar" style="left:778px;height:235px"><div class="bar-light"></div><div class="bar-dark"></div></div>
  <div class="pin" style="left:539px;top:714px">12</div>
  <div class="pin" style="left:599px;top:665px">27</div>
  <div class="pin" style="left:659px;top:632px">40</div>
  <div class="pin" style="left:719px;top:599px">49</div>
  <div class="pin" style="left:779px;top:551px">60</div>
  <div class="tick" style="left:547px">0°</div>
  <div class="tick" style="left:602px">15°</div>
  <div class="tick" style="left:662px">30°</div>
  <div class="tick" style="left:722px">45°</div>
  <div class="tick" style="left:782px">60°</div>
  <div class="abs axis-x">DEGREES OF FORWARD HEAD LIMIT</div>
  <div class="abs axis-y">PRESSURE SPINE(LBS)</div>

  <svg class="abs donut" viewBox="0 0 108 108">
    <circle cx="54" cy="54" r="52" fill="#ffffff" stroke="#e2e2e2" stroke-width="2"/>
    <circle cx="54" cy="54" r="45" fill="#bfe19b"/>
    <path d="M54 54 L54 9 A45 45 0 0 1 78 92 Z" fill="#1a6db5"/>
    <circle cx="54" cy="54" r="16" fill="#ffffff"/>
    <circle cx="54" cy="54" r="10" fill="#1a6db5"/>
  </svg>
  <div class="abs stat">
    <span class="g">THE AVERAGE PERSON</span><br>
    <span class="b">SPENDS 8-12 HOURS PER</span><br>
    <span class="b">DAY</span> <span class="g">USING ELECTRONIC</span><br>
    <span class="g">DEVICES</span>
  </div>

  <div class="abs footer-band"></div>
  <div class="abs location-card">
    <div class="doctor">DR. SAMUEL PORTER</div>
    <div class="now-in">NOW IN NORTHPORT AT</div>
    <div class="address">42 HARBOUR RD - MARKET SUITES</div>
  </div>
  <div class="abs offer">
    <div class="offer-pct">50%</div>
    <div class="offer-off">OFF</div>
    <div class="offer-note">INITIAL CONSULTATION</div>
  </div>
  <div class="abs booking">IF YOU BOOK ONLINE AT www.spinewellcare.example</div>
</main>
</body>
</html>
```